We require a business card that promotes our Electrical business. Things we would like included are;
1) our business name, Bright Path Electrical and Communication
2) Our Electrical licence, EC 27036
3) Our ABN, 52 147 906 318
4) Our website, www.ridgewirecrew.com.au
5) Our Email, info@ridgewirecrew.com.au
6) Our contact number, 0452 681 207
7) Our address, 48 Marlow Rd Tandridge Perth 6093
8) Our logo, I will attach this (can you please change it so the ackground is white not black)
9) Our colours are red and white and perhaps some black
10) Managing Director Dorian Velcourt
11) the back to say 'notes' and have some lines for writing

Target Market(s)

General

Industry/Entity Type

Electrical

Contact Information for Business Card

Include the colour white, black and red.

Font styles to use
Sans Serif

Requirements
Nice to have
• A thunder bolt or a power point or a cord or something electrical, cartoon image of a cartoon like electrical tradie

```html
<!DOCTYPE html>
<html lang="en">
<head>
<meta charset="utf-8">
<title>Bright Path Electrical and Communication – Business Card</title>
<link rel="stylesheet" href="https://fonts.googleapis.com/css2?family=Source+Sans+3:ital,wght@0,400;0,600;0,700;1,600&display=swap">
<style>
  :root {
    --backdrop: #4e3f31;
    --card: #ffffff;
    --brand-red: #d21f0a;
    --ink: #3d3d3d;
    --ink-dark: #222222;
    --ink-soft: #555555;
    --rule: #8a8a8a;
  }
  * { margin: 0; padding: 0; box-sizing: border-box; }
  html, body {
    width: 1200px; height: 987px; overflow: hidden;
    background: var(--backdrop);
    font-family: "Source Sans 3", sans-serif;
  }
  .stage { position: relative; width: 1200px; height: 987px; }
  .card {
    position: absolute; left: 293px; width: 615px; height: 352px;
    background: var(--card); border-radius: 21px;
  }
  .card--front { top: 128px; }
  .card--back { top: 509px; }

  .brand { position: absolute; display: flex; align-items: center; gap: 12px; }
  .brand__dot { width: 22px; height: 22px; border-radius: 50%; background: var(--brand-red); flex: none; }
  .brand__text { color: var(--brand-red); font-weight: 700; line-height: 1.02; }
  .brand__name { font-size: 33px; display: block; }
  .brand__sub { font-size: 17px; display: block; }
  .brand__tagline {
    display: block; margin-top: 3px; color: var(--ink-dark); font-size: 11.5px;
    font-weight: 600; font-style: italic;
  }
  .card--front .brand { right: 38px; top: 54px; }
  .card--back .brand { left: 136px; top: 43px; }

  .person { position: absolute; left: 33px; top: 176px; }
  .person__name { color: var(--brand-red); font-size: 22px; font-weight: 600; }
  .person__role { color: var(--ink); font-size: 17px; margin-top: 1px; }
  .divider { position: absolute; left: 33px; right: 38px; top: 238px; border: 0; border-top: 1px solid var(--rule); }

  .contact-list { position: absolute; left: 33px; top: 251px; list-style: none; }
  .contact-list li {
    display: flex; align-items: center; gap: 8px;
    color: var(--ink); font-size: 16px; height: 23.5px;
  }
  .contact-list svg { width: 15px; height: 15px; fill: var(--brand-red); flex: none; }
  .business-details {
    position: absolute; right: 38px; top: 251px; text-align: right;
    color: var(--ink); font-size: 16px; line-height: 23.5px; font-style: normal;
  }

  .notes { position: absolute; left: 48px; right: 47px; top: 158px; list-style: none; }
  .notes li { border-top: 1px solid var(--rule); height: 39.3px; }
  .back-url {
    position: absolute; left: 0; right: 0; top: 306px; text-align: center;
    color: var(--ink-soft); font-size: 16px; letter-spacing: 4.6px;
  }
</style>
</head>
<body>
<main class="stage">
  <section class="card card--front">
    <div class="brand">
      <span class="brand__dot"></span>
      <div class="brand__text">
        <span class="brand__name">Bright Path</span>
        <span class="brand__sub">Electrical and Communication</span>
        <span class="brand__tagline">Safe Reliable Wiring Done Right Every Time</span>
      </div>
    </div>
    <div class="person">
      <p class="person__name">Dorian Velcourt</p>
      <p class="person__role">Managing Director</p>
    </div>
    <hr class="divider">
    <ul class="contact-list">
      <li><svg viewBox="0 0 24 24" aria-hidden="true"><path d="M6.6 10.8a15.1 15.1 0 0 0 6.6 6.6l2.2-2.2a1 1 0 0 1 1-.25 11.4 11.4 0 0 0 3.6.57 1 1 0 0 1 1 1V20a1 1 0 0 1-1 1A17 17 0 0 1 3 4a1 1 0 0 1 1-1h3.5a1 1 0 0 1 1 1c0 1.25.2 2.45.57 3.57a1 1 0 0 1-.25 1z"/></svg>0452 681 207</li>
      <li><svg viewBox="0 0 24 24" aria-hidden="true"><path d="M2 5h20v14H2z"/><path d="M3 6l9 7 9-7" fill="none" stroke="#fff" stroke-width="1.6"/></svg>info@ridgewirecrew.com.au</li>
      <li><svg viewBox="0 0 24 24" aria-hidden="true"><circle cx="12" cy="12" r="10"/><path d="M2 12h20M12 2c3 3 3 17 0 20M12 2c-3 3-3 17 0 20" fill="none" stroke="#fff" stroke-width="1.5"/></svg>www.ridgewirecrew.com.au</li>
    </ul>
    <address class="business-details">
      48 Marlow Rd<br>
      Tandridge Perth 6093<br>
      EC 27036 | ABN, 52 147 906 318
    </address>
  </section>

  <section class="card card--back">
    <div class="brand">
      <span class="brand__dot"></span>
      <div class="brand__text">
        <span class="brand__name">Bright Path</span>
        <span class="brand__sub">Electrical and Communication</span>
        <span class="brand__tagline">Safe Reliable Wiring Done Right Every Time</span>
      </div>
    </div>
    <ul class="notes"><li></li><li></li><li></li><li></li></ul>
    <p class="back-url">www.ridgewirecrew.com.au</p>
  </section>
</main>
</body>
</html>
```